Influencer for sustainable living needs Youtube banner.

We are launching a Youtube Channel called "Reachable Greenway With Dorian Matusek" and need a Youtube design banner that will represent the channel's theme, branding, and content. The size of the banner must be 2560 x 1440 pixels with an optimized area of 1546 x 423 pixels that views well on all device types.

The banner needs to have the title of the channel, the subline of the types of content (Tours | DIY Guides | Inspiration), and display Dorian Matusek or his face. I have attached a picture of Dorian. We are open to using it as is or stylized.

The 3 types of Pillar content on the channel are:
1) Tours of sustainable properties and homes.
2) DIY educational and instructional videos.
3) Inspirational talks and interviews on sustainability and Permaculture.

The main purpose of the channel is to build our larger audience, increase trust and authority, and direct traffic to our paid educational offerings. Our paid educational offerings are hosted at “ReachableGreenwayCollege.example”. Click through the website to better understand our branding & offerings. (Brand Manual and logo also attached)

The "influencer" is the founder of the College - Dorian Matusek. He is a passionate, charismatic, and cheerful personality, who believes in the potential of humanity to create landscapes that thrive, so we can thrive within them. His core message is that humans can prove they are not a parasite by getting their homes, gardens, and communities in order so they shelter and feed us.

Files attached include versions of our logo and a branding manual for the College (note: the branding manual does not need to be followed exactly as it for the College (ReachableGreenwayCollege.example) and not the Youtube channel (Reachable Greenway With Dorian Matusek)... but the youtube channel branding should be similar.

Target Market(s)

DIYers, home owners, property owners, sustainable minded people, gardeners, homesteaders

Industry/Entity Type

Education, Sustainable living, Permaculture, Lifestyle

Font styles to use
Other font styles liked:
• Roboto & Urbanist. See design manual.

Requirements
Must have
• Clean and bright design. Not cliche. Use of colours, fonts, and more from brand manual.
Nice to have
• I would like to see banner which compares to other professional youtubers.

```html
<!DOCTYPE html>
<html lang="en">
<head>
<meta charset="utf-8">
<title>Reachable Greenway With Dorian Matusek – Channel Banner</title>
<link href="https://fonts.googleapis.com/css2?family=Caveat+Brush&family=Roboto:wght@500;700&family=Urbanist:wght@600&display=swap" rel="stylesheet">
<style>
  :root {
    --navy: #0b3f5f;
    --lime: #c3d52f;
    --lime-deep: #adc437;
    --teal: #57c3b7;
    --teal-soft: #62c4b5;
    --field-top: #5fae8c;
    --field-low: #4f9f7e;
    --white: #ffffff;
  }
  * { margin: 0; padding: 0; box-sizing: border-box; }
  html, body { width: 1200px; height: 675px; overflow: hidden; }
  body { position: relative; background: var(--field-top); }

  .backdrop-photo {
    position: absolute; inset: 0;
    background: linear-gradient(180deg, #6cb99a 0%, var(--field-top) 30%, var(--field-low) 100%);
  }

  .channel-band {
    position: absolute; left: 0; top: 238px; width: 1200px; height: 198px;
    background: var(--navy); overflow: hidden;
  }

  .hill-illustration {
    position: absolute; left: 0; top: 0; width: 575px; height: 198px;
    background: linear-gradient(180deg, #0f4a3f 0%, #1f6a3c 45%, #184f35 75%, var(--navy) 100%);
    -webkit-mask-image: linear-gradient(90deg, #000 80%, transparent 100%);
            mask-image: linear-gradient(90deg, #000 80%, transparent 100%);
  }

  .brand-lockup {
    position: absolute; left: 240px; top: 49px; height: 100px;
    display: flex; align-items: center; gap: 28px;
  }
  .brand-mark { width: 66px; height: 66px; background: var(--lime); border-radius: 6px; }
  .brand-name {
    font-family: "Urbanist", sans-serif; font-weight: 600;
    font-size: 35px; line-height: 36px; color: var(--white);
  }

  .with-word {
    position: absolute; left: 574px; top: 70px; z-index: 2;
    font-family: "Caveat Brush", cursive; font-size: 34px; line-height: 36px;
    color: var(--lime-deep); transform: rotate(-6deg);
  }

  .accent-shapes { position: absolute; left: 0; top: 0; }

  .host-portrait {
    position: absolute; left: 942px; top: 6px; width: 190px; height: 192px;
    background: linear-gradient(180deg, #8a6f62 0%, #b8907e 40%, #2f4566 62%, #23375a 100%);
    border-radius: 90px 90px 0 0;
  }

  .content-strip {
    position: absolute; left: 643px; top: 93px; width: 310px; height: 42px; z-index: 1;
    background: var(--teal-soft); border-radius: 20px 6px 14px 22px;
  }

  .host-name {
    position: absolute; left: 659px; top: 54px; z-index: 2;
    font-family: "Roboto", sans-serif; font-weight: 700;
    font-size: 38px; line-height: 42px; color: var(--white); white-space: nowrap;
  }
  .host-name .surname { color: var(--lime); }

  .content-pillars {
    position: absolute; left: 661px; top: 101px; z-index: 2;
    font-family: "Roboto", sans-serif; font-weight: 500;
    font-size: 19px; line-height: 26px; color: var(--navy); white-space: nowrap;
  }
</style>
</head>
<body>
  <div class="backdrop-photo" role="img" aria-label="Soft green-tinted photo of a garden homestead with a small metal-roofed house among trees"></div>

  <section class="channel-band">
    <div class="hill-illustration" role="img" aria-label="Watercolour illustration of green rolling hills with trees"></div>

    <div class="brand-lockup">
      <span class="brand-mark"></span>
      <span class="brand-name">Reachable<br>Greenway</span>
    </div>

    <span class="with-word">with</span>

    <svg class="accent-shapes" width="1200" height="198" viewBox="0 0 1200 198" aria-hidden="true">
      <path d="M1052 0 H1200 V198 H1130 C1110 160 1090 120 1092 80 C1094 45 1070 20 1052 0 Z" fill="var(--lime-deep)"/>
      <path d="M937 0 H1052 C1078 22 1098 48 1097 82 C1096 120 1118 160 1135 198 H960 C955 150 960 90 990 50 C970 30 950 18 937 0 Z" fill="var(--teal)"/>
    </svg>

    <div class="content-strip"></div>

    <div class="host-portrait" role="img" aria-label="Portrait of host Dorian Matusek smiling, wearing a navy jacket"></div>

    <h1 class="host-name">Dorian <span class="surname">Matusek</span></h1>
    <p class="content-pillars">Tours | DIY Guides | Inspiration</p>
  </section>
</body>
</html>
```